Kesrow Consulting- executive coaching business

looking for business card design for a newly started coaching business.
specialising in Exective coaching, Leadership, NLP and Motivation.
Looking for a simple, classy design using the existing logo attached and colour themes that complement the logo.
No red or orange in the business card design please.

Target Market(s)

Defence and Veteran community

Industry/Entity Type

Life Coaching

Contact Information for Business Card

looking for business cards for newly started coaching business.
specialising in Exective Coaching, Leadership, NLP and Motivation

Font styles to use
Serif
Script

Colors
0556a4
3176b5
86cfc6
33b8a4

Requirements
Must have
• Logo
• Email address- Lena@kesrowconsulting.com.au
• Contact number
• Services provided - Executive Coaching, Leadership, NLP and Motivation Profiling.
Nice to have
• Same colours as logo
Should not have
• Red or orange

```html
<!DOCTYPE html>
<html lang="en">
<head>
<meta charset="utf-8">
<title>Kesrow Consulting – Business Card</title>
<link href="https://fonts.googleapis.com/css2?family=Lato:wght@400;700&family=Montserrat:wght@600&display=swap" rel="stylesheet">
<style>
  :root {
    --page-bg: #e6eaee;
    --card-white: #ffffff;
    --brand-blue: #3176b5;
    --deep-blue: #0556a4;
    --ring-grey: #8a8d90;
    --faint-ring: #eef0f2;
    --ink: #1d1d1f;
    --white: #ffffff;
  }
  * { margin: 0; padding: 0; box-sizing: border-box; }
  html, body {
    width: 1200px; height: 960px; overflow: hidden;
    background: var(--page-bg);
    font-family: "Lato", Arial, sans-serif;
  }
  .sheet {
    width: 1200px; height: 960px;
    display: flex; flex-direction: column; align-items: center; justify-content: center;
    gap: 56px;
  }
  .card {
    position: relative;
    width: 720px; height: 412px;
    overflow: hidden;
    box-shadow: 0 6px 18px rgba(0,0,0,0.12);
  }
  /* Front */
  .card--front { background: var(--card-white); }
  .card--front .base-band {
    position: absolute; left: 0; right: 0; bottom: 0; height: 12px;
    background: var(--brand-blue);
  }
  .faint-ring {
    position: absolute; right: -20px; top: 50px;
    width: 280px; height: 280px; border-radius: 50%;
    border: 4px solid var(--faint-ring);
  }
  .brand {
    position: absolute; left: 36px; top: 38px; width: 400px;
    display: flex; flex-direction: column; align-items: center; gap: 16px;
  }
  .brand__dot {
    width: 118px; height: 118px; border-radius: 50%;
    border: 3px solid var(--ring-grey);
  }
  .brand__name {
    font-family: "Montserrat", Arial, sans-serif; font-weight: 600;
    font-size: 33px; letter-spacing: 0.5px; text-transform: uppercase;
    color: var(--brand-blue); white-space: nowrap;
  }
  .holder {
    position: absolute; right: 50px; top: 238px;
    font-size: 27px; color: var(--brand-blue);
  }
  .contacts {
    position: absolute; left: 62px; top: 298px;
    list-style: none; display: flex; flex-direction: column; gap: 6px;
    font-size: 21px; color: var(--ink);
  }
  .contacts li { display: flex; align-items: center; gap: 14px; }
  .contacts svg { width: 18px; height: 18px; flex: none; }
  /* Back */
  .card--back {
    background: var(--brand-blue);
    display: flex; flex-direction: column; align-items: center;
    padding-top: 66px;
  }
  .card--back .brand__dot { border-color: var(--white); width: 112px; height: 112px; }
  .card--back .brand__name { color: var(--white); margin-top: 18px; font-size: 38px; }
  .services {
    margin-top: 46px;
    font-size: 19px; letter-spacing: 0.6px; color: var(--white); white-space: nowrap;
  }
  .services .sep { margin: 0 8px; }
</style>
</head>
<body>
<main class="sheet">
  <section class="card card--front">
    <div class="faint-ring" aria-hidden="true"></div>
    <div class="brand">
      <div class="brand__dot" aria-hidden="true"></div>
      <div class="brand__name">Kesrow Consulting</div>
    </div>
    <p class="holder">Lena Marwick</p>
    <ul class="contacts">
      <li>
        <svg viewBox="0 0 24 24" aria-hidden="true"><path fill="#0556a4" d="M6.6 10.8a15.1 15.1 0 0 0 6.6 6.6l2.2-2.2a1 1 0 0 1 1-.25 11.4 11.4 0 0 0 3.6.57 1 1 0 0 1 1 1V20a1 1 0 0 1-1 1A17 17 0 0 1 3 4a1 1 0 0 1 1-1h3.5a1 1 0 0 1 1 1c0 1.25.2 2.45.57 3.57a1 1 0 0 1-.25 1z"/></svg>
        555 014 2270
      </li>
      <li>
        <svg viewBox="0 0 24 24" aria-hidden="true"><rect x="6" y="2" width="12" height="20" rx="2" fill="#0556a4"/><rect x="8" y="5" width="8" height="11" fill="#ffffff"/><circle cx="12" cy="19" r="1.2" fill="#ffffff"/></svg>
        555 014 2271
      </li>
      <li>
        <svg viewBox="0 0 24 24" aria-hidden="true"><rect x="2" y="5" width="20" height="14" fill="#0556a4"/><path d="M3 6l9 7 9-7" fill="none" stroke="#ffffff" stroke-width="1.6"/></svg>
        Lena@kesrowconsulting.com.au
      </li>
    </ul>
    <div class="base-band" aria-hidden="true"></div>
  </section>

  <section class="card card--back">
    <div class="brand__dot" aria-hidden="true"></div>
    <div class="brand__name">Kesrow Consulting</div>
    <p class="services">
      Executive Coaching<span class="sep">•</span>Leadership<span class="sep">•</span>NLP<span class="sep">•</span>Motivation Profiling
    </p>
  </section>
</main>
</body>
</html>
```